Bioidentical Hormone Replacement Therapy

I need a rectangular brochure- sized flyer (one page) designed to hand out to patients that will capture their attention. The flyer will display our company name, logo, contact information, website and social media information provided below. We need people to know that we offer a personalized approach to medicine. The main purpose of the flyer is to convey the fact that we offer bioidentical hormone replacement therapy (BHRT) for women and men by a pellet insertion procedure even for non members. Symptoms this can help with are for Women:
Fatigue*
Trouble sleeping*
Irritability*
Anxiousness*
Mood swings*
Low mood*
Night sweats*
Hot flashes or flushes*
Weight gain*
Decreased sex drive*
Discomfort during intercourse*
Low bone density*
and for Men:
Low sex drive*
Increased body fat
(especially in the waist area)*
Loss of muscle mass and strength*
Reduced mental focus*
Feelings of anxiety*
Irritability*
Fatigue*
Elevated blood sugar*
High cholesterol*
Practice name: Harborview Internal Medicine
Address: 4380 Quillmore Lane, Columbia, SC. 20281
Phone: 803-617-4953
Email: jbarlow@harborviewintmed.example
Website: https://harborviewintmed.example
Facebook: https://www.facebook.com/profile.php?id=73918265047721
For sizing 3.5 inch or so by 8.5 inch or so inch is fine. Not sure what is standard printing paper size for flyer.
Target Market(s)
Medical Patients
Industry/Entity Type
Healthcare
Look and feel

```html
<!DOCTYPE html>
<html lang="en">
<head>
<meta charset="utf-8">
<title>Natural Hormone for Women and Men – Harborview Internal Medicine</title>
<link href="https://fonts.googleapis.com/css2?family=Bebas+Neue&family=Montserrat:wght@300;400;600;700&display=swap" rel="stylesheet">
<style>
  :root{
    --blue:#3f63b3;
    --blue-dark:#3557a6;
    --ink:#262834;
    --footer-dark:#2e303d;
    --stage:#c9c9cc;
    --white:#ffffff;
    --photo-a:#e9dccd;
    --photo-b:#b9c6df;
  }
  *{margin:0;padding:0;box-sizing:border-box}
  html,body{width:1200px;height:2356px;overflow:hidden;background:var(--stage)}
  .flyer{
    position:absolute;left:60px;top:480px;width:990px;height:1280px;
    transform:scale(1.0909);transform-origin:0 0;
    background:var(--white);overflow:hidden;
    font-family:'Montserrat',sans-serif;color:var(--ink);
  }
  .hero-art{position:absolute;left:0;top:0;width:990px;height:720px}
  .headline{position:absolute;left:42px;top:62px;font-family:'Bebas Neue',sans-serif;line-height:.78}
  .headline .accent{display:block;color:var(--blue);font-size:122px}
  .headline .main{display:block;color:var(--ink);font-size:104px;line-height:.8;margin-top:4px}
  .rule{position:absolute;height:5px;background:var(--ink)}
  .headline-rule{left:42px;top:428px;width:84px}
  .subhead{position:absolute;left:42px;top:458px;font-weight:700;font-size:23px;line-height:24px;letter-spacing:.5px}
  .practice-mark{
    position:absolute;left:392px;top:410px;width:250px;height:250px;border-radius:50%;
    background:var(--white);display:flex;align-items:center;justify-content:center;text-align:center;
    font-weight:700;font-size:22px;line-height:28px;color:var(--ink);letter-spacing:1px;text-transform:uppercase;
  }
  .advantages-title{position:absolute;left:42px;top:697px;font-family:'Bebas Neue',sans-serif;font-size:41px;letter-spacing:.5px}
  .advantages{position:absolute;left:0;top:745px;width:255px;list-style:none}
  .advantages li{
    height:75px;margin-bottom:2px;padding:8px 0 0 42px;background:linear-gradient(var(--blue),var(--blue-dark));
    color:var(--white);font-weight:700;font-size:22px;line-height:28px;letter-spacing:1.2px;
  }
  .symptoms{position:absolute;top:693px}
  .symptoms.women{left:288px}
  .symptoms.men{left:600px}
  .symptoms h2{font-weight:300;font-size:30px;line-height:30px;letter-spacing:1px}
  .symptoms h2 strong{font-weight:700}
  .symptoms .rule{position:static;display:block;width:34px;height:3px;margin:10px 0 8px}
  .symptoms ul{list-style:none}
  .symptoms li{position:relative;padding-left:26px;font-size:18.5px;line-height:24px;letter-spacing:.3px;white-space:nowrap}
  .symptoms li svg{position:absolute;left:0;top:5px;width:16px;height:16px}
  .footer-art{position:absolute;left:0;top:1100px;width:990px;height:180px}
  .contact{position:absolute;left:45px;top:1120px;list-style:none;color:var(--white);font-size:17.5px;line-height:24.5px}
  .contact li{position:relative;padding-left:25px}
  .contact li svg{position:absolute;left:0;top:5px;width:15px;height:15px}
  .contact .phone{font-weight:600}
  .doctor{position:absolute;left:450px;top:1108px;width:300px;color:var(--white)}
  .doctor h3{font-family:'Bebas Neue',sans-serif;font-weight:400;font-size:36px;line-height:40px;letter-spacing:-.3px;white-space:nowrap}
  .doctor .specialty{font-weight:300;font-size:25px;line-height:30px;letter-spacing:.5px}
  .doctor .rule{position:static;display:block;width:36px;height:2px;background:var(--white);margin:14px 0 16px}
  .doctor .tagline{font-weight:600;font-size:20.5px;line-height:26px}
  .doctor-photo{position:absolute;left:765px;top:1032px;width:215px;height:248px;
    background:linear-gradient(180deg,#e8c8b0 0%,#9c2732 48%,#7e1c26 100%);border-radius:100px 100px 0 0}
</style>
</head>
<body>
<main class="flyer">
  <svg class="hero-art" viewBox="0 0 990 720">
    <defs>
      <linearGradient id="photoTone" x1="0" y1="0" x2="1" y2="1">
        <stop offset="0" stop-color="var(--photo-a)"/>
        <stop offset="1" stop-color="var(--photo-b)"/>
      </linearGradient>
    </defs>
    <rect x="400" y="40" width="590" height="480" fill="url(#photoTone)" role="img" aria-label="Photo of a smiling mature couple embracing"/>
    <path d="M400 520 L400 470 C600 480 800 470 990 440 L990 720 L400 720 Z" fill="var(--white)"/>
    <path d="M640 515 C760 470 880 440 990 440 L990 500 C880 492 760 500 640 530 Z" fill="var(--ink)"/>
    <path d="M0 520 C80 600 250 625 430 615 L430 622 C250 645 90 640 0 575 Z" fill="var(--blue)"/>
  </svg>

  <h1 class="headline">
    <span class="accent">Natural</span>
    <span class="accent">Hormone</span>
    <span class="main">For Women</span>
    <span class="main">And Men</span>
  </h1>
  <span class="rule headline-rule"></span>
  <p class="subhead">BY A PELLET<br>INSERTION PROCEDURE</p>

  <div class="practice-mark">Harborview<br>Internal<br>Medicine</div>

  <h2 class="advantages-title">Our Advantages</h2>
  <ul class="advantages">
    <li>QUALIFIED<br>PROVIDER</li>
    <li>MODERN<br>CONVENIENCE</li>
    <li>PERSONALIZED<br>CARE</li>
    <li>INDIVIDUAL<br>APPROACH</li>
  </ul>

  <section class="symptoms women">
    <h2>SYMPTOMS<br>FOR <strong>WOMEN:</strong></h2>
    <span class="rule"></span>
    <ul>
      <li><svg viewBox="0 0 16 16"><circle cx="8" cy="8" r="8" fill="var(--blue)"/><path d="M4.5 8.3l2.3 2.3 4.7-4.9" stroke="#fff" stroke-width="2" fill="none"/></svg>Fatigue*</li>
      <li><svg viewBox="0 0 16 16"><circle cx="8" cy="8" r="8" fill="var(--blue)"/><path d="M4.5 8.3l2.3 2.3 4.7-4.9" stroke="#fff" stroke-width="2" fill="none"/></svg>Trouble sleeping*</li>
      <li><svg viewBox="0 0 16 16"><circle cx="8" cy="8" r="8" fill="var(--blue)"/><path d="M4.5 8.3l2.3 2.3 4.7-4.9" stroke="#fff" stroke-width="2" fill="none"/></svg>Irritability*</li>
      <li><svg viewBox="0 0 16 16"><circle cx="8" cy="8" r="8" fill="var(--blue)"/><path d="M4.5 8.3l2.3 2.3 4.7-4.9" stroke="#fff" stroke-width="2" fill="none"/></svg>Anxiousness*</li>
      <li><svg viewBox="0 0 16 16"><circle cx="8" cy="8" r="8" fill="var(--blue)"/><path d="M4.5 8.3l2.3 2.3 4.7-4.9" stroke="#fff" stroke-width="2" fill="none"/></svg>Mood swings*</li>
      <li><svg viewBox="0 0 16 16"><circle cx="8" cy="8" r="8" fill="var(--blue)"/><path d="M4.5 8.3l2.3 2.3 4.7-4.9" stroke="#fff" stroke-width="2" fill="none"/></svg>Low mood*</li>
      <li><svg viewBox="0 0 16 16"><circle cx="8" cy="8" r="8" fill="var(--blue)"/><path d="M4.5 8.3l2.3 2.3 4.7-4.9" stroke="#fff" stroke-width="2" fill="none"/></svg>Night sweats*</li>
      <li><svg viewBox="0 0 16 16"><circle cx="8" cy="8" r="8" fill="var(--blue)"/><path d="M4.5 8.3l2.3 2.3 4.7-4.9" stroke="#fff" stroke-width="2" fill="none"/></svg>Hot flashes or flushes*</li>
      <li><svg viewBox="0 0 16 16"><circle cx="8" cy="8" r="8" fill="var(--blue)"/><path d="M4.5 8.3l2.3 2.3 4.7-4.9" stroke="#fff" stroke-width="2" fill="none"/></svg>Weight gain*</li>
      <li><svg viewBox="0 0 16 16"><circle cx="8" cy="8" r="8" fill="var(--blue)"/><path d="M4.5 8.3l2.3 2.3 4.7-4.9" stroke="#fff" stroke-width="2" fill="none"/></svg>Decreased sex drive*</li>
      <li><svg viewBox="0 0 16 16"><circle cx="8" cy="8" r="8" fill="var(--blue)"/><path d="M4.5 8.3l2.3 2.3 4.7-4.9" stroke="#fff" stroke-width="2" fill="none"/></svg>Discomfort during intercourse*</li>
      <li><svg viewBox="0 0 16 16"><circle cx="8" cy="8" r="8" fill="var(--blue)"/><path d="M4.5 8.3l2.3 2.3 4.7-4.9" stroke="#fff" stroke-width="2" fill="none"/></svg>Low bone density*</li>
    </ul>
  </section>

  <section class="symptoms men">
    <h2>SYMPTOMS<br>FOR <strong>MEN:</strong></h2>
    <span class="rule"></span>
    <ul>
      <li><svg viewBox="0 0 16 16"><circle cx="8" cy="8" r="8" fill="var(--blue)"/><path d="M4.5 8.3l2.3 2.3 4.7-4.9" stroke="#fff" stroke-width="2" fill="none"/></svg>Low sex drive*</li>
      <li><svg viewBox="0 0 16 16"><circle cx="8" cy="8" r="8" fill="var(--blue)"/><path d="M4.5 8.3l2.3 2.3 4.7-4.9" stroke="#fff" stroke-width="2" fill="none"/></svg>Increased body fat</li>
      <li><svg viewBox="0 0 16 16"><circle cx="8" cy="8" r="8" fill="var(--blue)"/><path d="M4.5 8.3l2.3 2.3 4.7-4.9" stroke="#fff" stroke-width="2" fill="none"/></svg>(especially in the waist area)*</li>
      <li><svg viewBox="0 0 16 16"><circle cx="8" cy="8" r="8" fill="var(--blue)"/><path d="M4.5 8.3l2.3 2.3 4.7-4.9" stroke="#fff" stroke-width="2" fill="none"/></svg>Loss of muscle mass and strength*</li>
      <li><svg viewBox="0 0 16 16"><circle cx="8" cy="8" r="8" fill="var(--blue)"/><path d="M4.5 8.3l2.3 2.3 4.7-4.9" stroke="#fff" stroke-width="2" fill="none"/></svg>Reduced mental focus*</li>
      <li><svg viewBox="0 0 16 16"><circle cx="8" cy="8" r="8" fill="var(--blue)"/><path d="M4.5 8.3l2.3 2.3 4.7-4.9" stroke="#fff" stroke-width="2" fill="none"/></svg>Feelings of anxiety*</li>
      <li><svg viewBox="0 0 16 16"><circle cx="8" cy="8" r="8" fill="var(--blue)"/><path d="M4.5 8.3l2.3 2.3 4.7-4.9" stroke="#fff" stroke-width="2" fill="none"/></svg>Irritability*</li>
      <li><svg viewBox="0 0 16 16"><circle cx="8" cy="8" r="8" fill="var(--blue)"/><path d="M4.5 8.3l2.3 2.3 4.7-4.9" stroke="#fff" stroke-width="2" fill="none"/></svg>Fatigue*</li>
      <li><svg viewBox="0 0 16 16"><circle cx="8" cy="8" r="8" fill="var(--blue)"/><path d="M4.5 8.3l2.3 2.3 4.7-4.9" stroke="#fff" stroke-width="2" fill="none"/></svg>Elevated blood sugar*</li>
      <li><svg viewBox="0 0 16 16"><circle cx="8" cy="8" r="8" fill="var(--blue)"/><path d="M4.5 8.3l2.3 2.3 4.7-4.9" stroke="#fff" stroke-width="2" fill="none"/></svg>High cholesterol*</li>
    </ul>
  </section>

  <svg class="footer-art" viewBox="0 0 990 180" aria-hidden="true">
    <rect x="0" y="3" width="990" height="177" fill="var(--footer-dark)"/>
    <path d="M430 0 L990 0 L990 180 L375 180 Z" fill="var(--blue)"/>
  </svg>

  <ul class="contact">
    <li><svg viewBox="0 0 16 16"><path d="M8 1.5a4.6 4.6 0 0 0-4.6 4.6C3.4 9.6 8 14.5 8 14.5s4.6-4.9 4.6-8.4A4.6 4.6 0 0 0 8 1.5z" fill="none" stroke="#fff" stroke-width="1.4"/><circle cx="8" cy="6.1" r="1.6" fill="#fff"/></svg>4380 Quillmore Lane,<br>Columbia, SC. 20281</li>
    <li class="phone"><svg viewBox="0 0 16 16"><circle cx="8" cy="8" r="7" fill="none" stroke="#fff" stroke-width="1.3"/><path d="M5.3 4.6l1.4-.3.8 1.8-.9.7c.5 1 1.2 1.7 2.2 2.2l.7-.9 1.8.8-.3 1.4c-3 .2-5.9-2.7-5.7-5.7z" fill="#fff"/></svg>803-617-4953</li>
    <li><svg viewBox="0 0 16 16"><rect x="1.5" y="3.5" width="13" height="9" fill="none" stroke="#fff" stroke-width="1.3"/><path d="M1.5 3.8L8 9l6.5-5.2" fill="none" stroke="#fff" stroke-width="1.3"/></svg>jbarlow@harborviewintmed.example</li>
    <li><svg viewBox="0 0 16 16"><circle cx="8" cy="8" r="6.5" fill="none" stroke="#fff" stroke-width="1.2"/><ellipse cx="8" cy="8" rx="2.8" ry="6.5" fill="none" stroke="#fff" stroke-width="1.1"/><path d="M1.5 8h13" stroke="#fff" stroke-width="1.1"/></svg>www.harborviewintmed.example</li>
    <li><svg viewBox="0 0 16 16"><circle cx="8" cy="8" r="7.5" fill="#fff"/></svg>/profile.php?id=73918265047721</li>
  </ul>

  <div class="doctor">
    <h3>MARCUS R. DELANEY II, DO</h3>
    <p class="specialty">Internal Medicine</p>
    <span class="rule"></span>
    <p class="tagline">My Philosophy and<br>Approach to Wellness...</p>
  </div>
  <div class="doctor-photo" role="img" aria-label="Portrait photo of the physician in a maroon polo shirt"></div>
</main>
</body>
</html>
```